Holistic Psychology clinic flyer-

We need a 3 fold flyer that is both professional and zen looking with holistic elements- bilingual on both sides.
I am looking for a design that conveys the sense of confidence, yet relaxing to the eye and makes people want to pick it up and read it!
We are all about balance (yin, yang) and bringing equilibrium to a person in their quest to get better.

Target Market(s)

families adults, teens children experiencing mental health issues

Industry/Entity Type

Psychologist

Font styles to use
Serif

Colors
fbf289
cee9f5
0455a3

Requirements
Must have
• my logo (spiral) ; French one side; English on the other. Text is provided; Some color but clean, zen elements
• Easy to read text
Nice to have
• nature elements, bamboo? trees etc. sunrise or sunset?
• The sunset back ground provided in the picture is not necessary
• families?
Should not have
• too many distracting elements; not too many colors. colors must be subtle and must flow together

```html
<!DOCTYPE html>
<html lang="en">
<head>
<meta charset="utf-8">
<title>Clinique Serenova – Trifold Brochure</title>
<link rel="stylesheet" href="https://fonts.googleapis.com/css2?family=Noto+Serif:ital,wght@0,700;1,700&family=Tinos:ital,wght@0,400;0,700;1,700&display=swap">
<style>
  :root {
    --deep-blue: #1d4fa8;
    --brand-blue: #0455a3;
    --sky: #cee9f5;
    --sun: #fbf289;
    --ink: #14141e;
    --navy: #1c1f5e;
    --white: #ffffff;
    --page: #ffffff;
  }
  * { box-sizing: border-box; margin: 0; padding: 0; }
  html, body { width: 1200px; height: 1200px; overflow: hidden; background: var(--page); }
  body { font-family: "Tinos", "Times New Roman", serif; color: var(--ink); }

  .brochure {
    position: absolute; left: 60px; top: 180px;
    width: 1080px; height: 840px;
    display: flex;
    box-shadow: 0 10px 30px rgba(0,0,0,.18);
  }
  .panel {
    position: relative; width: 360px; height: 100%;
    background: linear-gradient(to bottom,
      var(--deep-blue) 0%, #4f86d0 14%, var(--sky) 32%,
      var(--sun) 55%, #f6f3c0 66%, #7fa9df 80%, var(--deep-blue) 100%);
    overflow: hidden;
  }
  .panel + .panel { border-left: 1px solid rgba(255,255,255,.35); }

  .panel-title {
    font-family: "Noto Serif", Georgia, serif; font-weight: 700;
    color: var(--white); font-size: 21px; margin: 56px 0 26px;
  }
  .services { padding: 0 34px 0 32px; }
  .service { margin-bottom: 18px; }
  .service h3 { font-size: 14px; font-weight: 700; line-height: 1.15; }
  .service p, .welcome p { font-size: 13.2px; line-height: 1.24; text-align: justify; }

  .welcome { padding: 0 30px; }
  .welcome p { margin-bottom: 16px; }
  .motto { text-align: center; font-size: 15.5px; line-height: 1.35; margin: 24px 0 28px; text-transform: uppercase; }
  .call { text-align: center; font-size: 15px; line-height: 1.3; margin-top: 6px; }
  .phone-big { text-align: center; color: var(--white); font-weight: 700; font-size: 22px; margin-top: 28px; }
  .email-big { text-align: center; color: var(--white); font-size: 17px; margin-top: 4px; }

  .cover { padding: 0; }
  .brand {
    display: flex; align-items: center; gap: 12px;
    margin: 70px 0 0 34px;
  }
  .brand-dot { width: 40px; height: 40px; border-radius: 50%; background: var(--sun); }
  .brand-name { font-family: "Tinos", serif; font-size: 52px; color: var(--navy); font-weight: 400; }
  .clinic-name {
    font-family: "Noto Serif", Georgia, serif; font-weight: 700;
    color: var(--navy); font-size: 29px; margin: 72px 0 0 32px;
  }
  .tagline {
    font-family: "Noto Serif", Georgia, serif; font-style: italic; font-weight: 700;
    font-size: 20px; line-height: 1.27; margin: 24px 0 0 34px; color: var(--ink);
  }
  .sunrise {
    position: absolute; left: 0; top: 370px; width: 360px; height: 150px;
  }
  .audience { list-style: none; position: absolute; top: 540px; left: 36px; }
  .audience li {
    font-style: italic; font-weight: 700; font-size: 17px; line-height: 1.5;
    display: flex; align-items: center; gap: 12px;
  }
  .audience li::before { content: ""; width: 8px; height: 8px; border-radius: 50%; background: var(--ink); }
  .contact {
    position: absolute; top: 680px; left: 0; width: 100%;
    text-align: center; font-size: 15px; line-height: 1.3; color: var(--ink);
  }
  .contact .tel { font-size: 17px; }
  .web-band {
    position: absolute; bottom: 26px; left: 0; width: 100%; height: 28px;
    background: var(--sun); color: var(--navy);
    font-size: 17px; letter-spacing: 6px; text-align: center; line-height: 28px;
  }
</style>
</head>
<body>
<main class="brochure">

  <section class="panel services">
    <h2 class="panel-title">Our Professional Services</h2>
    <article class="service">
      <h3>Clinical Psychology</h3>
      <p>Psychologists are people specialists. Learn how to better understand both yourself and those in your life. Release some of the emotional and relational distress that drains you. It's time for change!</p>
    </article>
    <article class="service">
      <h3>Integrative Psychotherapy</h3>
      <p>We distill the very best approaches in psychology to help you free your mind, balance your body and heal your spirit. We specialize in helping you understand and harmonize the mind-body connection.</p>
    </article>
    <article class="service">
      <h3>Life Coaching</h3>
      <p>Life's challenges are opportunities for your growth. Our life coaches are skilled, caring and passionate about supporting you. Come in, it's time to discover your potential!</p>
    </article>
    <article class="service">
      <h3>Sports Psychology</h3>
      <p>There are many different psychological benefits of sports. Our sports psychologists can work with you to release your mental blocks, improve your performance and ensure success! Dare to aim high!</p>
    </article>
    <article class="service">
      <h3>Psycho-Educational Assessments</h3>
      <p>With the aid of psychometric tests, we can help you to figure out how your mind or that of your child works. We will highlight strengths and give recommendations to remedy any weaknesses. A detailed report and an academic intervention plan is customized for individuals aged 4-64!</p>
    </article>
    <article class="service">
      <h3>Mindfulness Meditation Classes</h3>
      <p>Meditation is much more than a relaxation technique. Mindfulness will bring you a heightened awareness and improved quality of life. These classes are offered weekly and will be useful to you to learn how to meditate and integrate it into your daily life. Find your inner peace!</p>
    </article>
  </section>

  <section class="panel welcome">
    <h2 class="panel-title">Welcome to Serenova !</h2>
    <p>We present you with a whole new way of achieving wellness in your life. We offer a variety of clinical and educational services in a professional and peaceful environment. We use an integrative approach.</p>
    <p>We are delighted to present you with several effective and scientific approaches that can help you. We offer a variety of clinical and educational services in a professional and peaceful environment. We are committed to supporting you in reaching your potential and feeling better by adhering to an integrative mind-body approach.</p>
    <p>We are passionate about supporting you in reaching your potential and feeling well. It's time to start thinking of you...</p>
    <div class="motto">Calm your mind,<br>relax your body,<br>nourish your spirit.</div>
    <p>Mathieu Laroche, BSc, MA. is the founder and director of Serenova. As a clinical psychologist, author and motivational speaker with 26 years of experience, Mathieu is a pioneer in holistic psychology, an integrative approach that promotes healing and wellness. He and his staff are skilled in using cutting edge mind-body-spirit tools to help you with a variety of health, relational, educational and parenting issues. We look forward to supporting you and your family</p>
    <div class="call">Contact us today for a<br>free phone consultation</div>
    <div class="phone-big">514-555-0147</div>
    <div class="email-big">info@serenova.ca</div>
  </section>

  <section class="panel cover">
    <div class="brand">
      <span class="brand-dot"></span>
      <span class="brand-name">Serenova</span>
    </div>
    <h1 class="clinic-name">Clinique Serenova</h1>
    <p class="tagline">Psychologists<br>and Educational<br>Professionals<br>with an Integrative<br>Approach</p>
    <svg class="sunrise" role="img" aria-label="Illustration of a rising sun over the horizon with birds in flight" viewBox="0 0 360 150">
      <defs>
        <radialGradient id="sunGlow" cx="0.45" cy="0.95" r="0.6">
          <stop offset="0" stop-color="#ffffff" stop-opacity="0.95"/>
          <stop offset="0.45" stop-color="#fffbd8" stop-opacity="0.7"/>
          <stop offset="1" stop-color="#fbf289" stop-opacity="0"/>
        </radialGradient>
      </defs>
      <rect width="360" height="150" fill="url(#sunGlow)"/>
    </svg>
    <ul class="audience">
      <li>Children</li>
      <li>Teens</li>
      <li>Adults</li>
      <li>Couples</li>
    </ul>
    <address class="contact" style="font-style:normal">
      4580 Rue des Érables, Beaconsfield,<br>
      Québec H9W 2K3<br>
      <span class="tel">Tel: (514) 555-0147</span><br>
      info@serenova.ca<br>
      www.facebook.com/Serenova
    </address>
    <div class="web-band">www.serenova.ca</div>
  </section>

</main>
</body>
</html>
```